Business Card Design to Compliment attached Letterhead

I am looking for a really nice business card for my new business launch. I develop Excel based applications to support administrative and operational processes. I have attached my letterhead so you have an idea what the components should look like. I tried uploading the various components into the "Design your own" section, but they looked really rough, so I am looking for someone to be able to come up with a nice crisp version of the tetras square and the Company Name styling that will compliment my letterhead; and then put all of this into a business card design that is crisp, clean and professional looking. I am considering using spot gloss, because I think it will add an extra touch of class.

Industry/Entity Type

Business

Contact Information for Business Card

Pendrix Consulting, Tabula Remedies for Weekday Puzzles, Mirela Dunstan, Business Systems Analyst, Spreadsheet Specialist, 0438 270 915, mirela@pendrixconsulting.com.au www.pendrixconsulting.com.au

Requirements
Must have
• I want to use the same colors as the attached file and keep the fonts used for "Pendrix" and "Consulting"
• I need the Tetras square to be re-created. I did it myself using photoshop and it is pretty rough. I need it to be crisp and clean and professional looking.
• Please include my name, title, phone, email, web address and "Tabula Remedies to Weekday Puzzles"
Nice to have
• So far I have liked the designs that are a little bit different. I want people to look at my card and say "Nice Card"
Should not have
• I don't like the see-through format.
• Do not include any information about Quorra Ventures or the address
• Please dont use my version of the tetras square, it is fuzzy and poorly drawn (I did it myself), I need it to be crisp, and clean otherwise it will spoil the effect of my nice new cards.

```html
<!DOCTYPE html>
<html lang="en">
<head>
<meta charset="utf-8">
<title>Pendrix Consulting – Business Card</title>
<link href="https://fonts.googleapis.com/css2?family=Open+Sans:wght@400;600;700&display=swap" rel="stylesheet">
<style>
  :root {
    --backdrop: #3b3b3d;
    --card: #ffffff;
    --brand-blue: #1d87c8;
    --brand-purple: #7a3ea6;
    --ink: #2b2b2b;
  }
  * { box-sizing: border-box; margin: 0; padding: 0; }
  html, body {
    width: 1200px; height: 852px; overflow: hidden;
    background: var(--backdrop);
    font-family: "Open Sans", Arial, sans-serif;
  }
  .stage {
    width: 1200px; height: 852px;
    display: flex; align-items: center; justify-content: center; gap: 50px;
  }
  .card {
    position: relative;
    width: 500px; height: 290px;
    background: var(--card);
    border-radius: 12px;
    overflow: hidden;
    box-shadow: 0 10px 24px rgba(0,0,0,.35);
  }
  .brand {
    display: flex; align-items: center; gap: 12px;
    color: var(--brand-purple);
    font-weight: 700;
    white-space: nowrap;
  }
  .brand-square {
    background: var(--brand-blue);
    flex: none;
  }
  .card-front .brand {
    position: absolute; left: 50%; top: 50%;
    transform: translate(-50%, -50%);
    font-size: 40px;
  }
  .card-front .brand-square { width: 44px; height: 44px; }
  .card-back .brand {
    position: absolute; right: 30px; top: 32px;
    font-size: 24px;
  }
  .card-back .brand-square { width: 26px; height: 26px; }
  .holder { position: absolute; left: 32px; top: 96px; }
  .holder-name { color: var(--brand-blue); font-weight: 700; font-size: 16px; }
  .holder-role { color: var(--ink); font-size: 11px; line-height: 15px; }
  .contacts {
    position: absolute; left: 32px; top: 178px;
    list-style: none;
  }
  .contacts li {
    display: flex; align-items: center; gap: 10px;
    font-size: 12.5px; color: var(--ink); line-height: 19px;
  }
  .contacts svg { width: 12px; height: 12px; fill: var(--brand-blue); flex: none; }
  .tagline {
    position: absolute; left: 32px; top: 240px;
    color: var(--brand-purple); font-size: 13px;
  }
  .bands { position: absolute; inset: 0; }
</style>
</head>
<body>
<main class="stage">
  <section class="card card-front" aria-label="Card front">
    <div class="brand"><span class="brand-square"></span>Pendrix Consulting</div>
  </section>

  <section class="card card-back" aria-label="Card back">
    <svg class="bands" viewBox="0 0 500 290" aria-hidden="true">
      <polygon points="300,262 500,196 500,210 300,272" fill="var(--brand-purple)"/>
      <polygon points="0,276 300,272 500,210 500,290 0,290" fill="var(--brand-blue)"/>
    </svg>
    <div class="brand"><span class="brand-square"></span>Pendrix Consulting</div>
    <div class="holder">
      <h1 class="holder-name">Mirela Dunstan</h1>
      <p class="holder-role">Business Systems Analyst</p>
      <p class="holder-role">Spreadsheet Specialist</p>
    </div>
    <ul class="contacts">
      <li><svg viewBox="0 0 24 24"><path d="M6.6 10.8a15.1 15.1 0 0 0 6.6 6.6l2.2-2.2a1 1 0 0 1 1-.25 11.4 11.4 0 0 0 3.6.57 1 1 0 0 1 1 1V20a1 1 0 0 1-1 1A17 17 0 0 1 3 4a1 1 0 0 1 1-1h3.5a1 1 0 0 1 1 1c0 1.25.2 2.45.57 3.6a1 1 0 0 1-.25 1z"/></svg>0438 270 915</li>
      <li><svg viewBox="0 0 24 24"><path d="M2 5h20v14H2z M3.5 6.5 12 13l8.5-6.5" fill="none" stroke="var(--brand-blue)" stroke-width="2"/></svg>mirela@pendrixconsulting.com.au</li>
      <li><svg viewBox="0 0 24 24"><circle cx="12" cy="12" r="9" fill="none" stroke="var(--brand-blue)" stroke-width="2"/><path d="M3 12h18M12 3c3 3 3 15 0 18M12 3c-3 3-3 15 0 18" fill="none" stroke="var(--brand-blue)" stroke-width="1.6"/></svg>www.pendrixconsulting.com.au</li>
    </ul>
    <p class="tagline">Tabula Remedies for Weekday Puzzles</p>
  </section>
</main>
</body>
</html>
```